New Sports Team- Womens Football

New team in San Diego.  Looking for a website that can be updated by us after the design is established.
Pages needed:
About us
Roster
Coaches/Staff
Schedule
Online Store (This link will go out to an external vendor)
Community Partners /Sponsors
Some good team pages to take a look at:
lakeportkestrels.example
brimfieldtidewatchfootball.example

Please use the logo I attempted to upload.  Looking for Flash Intro that incorporates the definition of the word "VANTA" and then the logo appearing.
Use the following words:
;any sudden, strong increase, as of energy, enthusiasm, etc.
;To improve one's performance suddenly, especially in bettering one's standing in a competition.

I placed a couple more pictures.
Adding another version of the team logo. In all designs I have seen thus far, everyone has the logo very small and it appears transparent. Might help to have the jpeg version. Also added some more photos
We are approaching the deadline quickly. Just a few last notes to the designs I have been viewing. All designs that are not close to the brief will be eliminated.

```html
<!DOCTYPE html>
<html lang="en">
<head>
<meta charset="utf-8">
<title>VANTA Womens Football</title>
<link href="https://fonts.googleapis.com/css2?family=Ubuntu:wght@400;500;700&family=Arimo:ital,wght@0,400;0,700;1,400&family=Tinos:ital@1&display=swap" rel="stylesheet">
<style>
:root{
  --header-dark:#23272e;
  --header-stripe:#2c3039;
  --page-blue:#1a70a8;
  --page-blue-light:#2b8cc6;
  --panel-edge:#8fc3e6;
  --white:#ffffff;
  --ink:#222;
  --grey:#6b6b6b;
  --muted:#999;
  --rule:#b9b9b9;
  --red:#cc1111;
  --navy:#163a6b;
  --green:#6a9a2a;
  --orange:#e06a10;
  --cal-cell:#a9c8e2;
  --cal-today:#1b6ea6;
  --tile-border:#dcdcdc;
}
*{box-sizing:border-box;margin:0;padding:0}
html,body{width:1003px;height:1200px;overflow:hidden}
body{position:relative;background:linear-gradient(180deg,var(--page-blue-light) 0,var(--page-blue) 60%,#14669c 100%);font-family:Arimo,Arial,sans-serif;color:var(--ink)}
.abs{position:absolute}
.header{position:absolute;left:0;top:0;width:1003px;height:133px;background:repeating-linear-gradient(135deg,var(--header-dark) 0 10px,var(--header-stripe) 10px 20px)}
.header-rule{position:absolute;left:0;top:133px;width:1003px;height:4px;background:var(--white)}
.social{position:absolute;top:39px;display:flex;align-items:center;gap:4px;font:500 11px Ubuntu,sans-serif;color:var(--white)}
.social i{display:block;width:10px;height:10px;background:var(--page-blue-light)}
.nav a{position:absolute;top:111px;font:700 13px Ubuntu,sans-serif;color:var(--white);text-decoration:none}
.nav a.current::after{content:"";position:absolute;left:50%;top:21px;margin-left:-5px;border:5px solid transparent;border-bottom-color:var(--white)}
.brand{position:absolute;left:392px;top:8px;width:220px;height:170px;display:flex;flex-direction:column;align-items:center;justify-content:center;gap:6px}
.brand span{font:700 46px Ubuntu,sans-serif;color:var(--white);letter-spacing:2px}
.brand i{width:14px;height:14px;border-radius:50%;background:var(--white)}
.search{position:absolute;left:639px;top:40px;width:239px;height:27px;display:flex;border:1px solid #ccc;background:var(--white)}
.search .field{flex:1;display:flex;align-items:center;gap:6px;padding-left:8px;font-size:11px;color:#555}
.search .go{width:45px;border-left:1px solid #bbb;background:linear-gradient(#fafafa,#ddd);font:700 11px Arimo,sans-serif;display:flex;align-items:center;justify-content:center;color:#333}
.panel{position:absolute;left:120px;top:190px;width:764px;height:956px;background:var(--white);border:6px solid var(--panel-edge);border-radius:10px}
.ph{background:linear-gradient(180deg,#9aa08a 0,#7fae5a 25%,#6ea34c 100%);border:1px solid #888}
.h2{font:400 16px Ubuntu,sans-serif;color:var(--ink)}
.h2.red{color:var(--red)}
.h2.navy{color:var(--navy)}
.small-link{font:400 9.5px Ubuntu,sans-serif;color:#333}
.tiles{position:absolute;left:598px;top:231px;display:grid;grid-template-columns:repeat(4,61px);gap:7px}
.tile{height:61px;border:1px solid var(--tile-border);border-radius:4px;background:#f4f4f4;display:flex;align-items:center;justify-content:center;box-shadow:inset 0 0 0 4px #fff;font-size:8px;color:#aaa}
.hr{position:absolute;height:0;border-top:1px dotted var(--rule)}
.vr{position:absolute;width:0;border-left:1px dotted var(--rule)}
.bullet{position:relative;padding-left:14px}
.bullet::before{content:"";position:absolute;left:0;top:3px;width:5px;height:5px;border:2px solid #999;border-radius:50%}
.news-item{position:absolute;left:146px;width:200px}
.news-item b{font-size:11px;color:#333}
.news-item .meta{font:italic 10.5px Tinos,serif;color:#444;margin-top:3px}
.news-item p{font-size:11px;color:var(--grey);line-height:15px}
.recent{position:absolute;left:384px;top:520px;width:240px;font-size:11px;color:var(--grey);line-height:15px}
.recent strong{color:#555}
.recent ul{list-style:none;margin-top:8px}
.recent li{font-weight:700;color:var(--red);margin-bottom:10px}
.blog{position:absolute;left:655px;width:200px;font-size:11px;line-height:15px;color:var(--grey)}
.blog b{color:var(--green);font-size:11.5px}
.blog .meta{font:italic 11px Tinos,serif;color:#333}
.calendar{position:absolute;left:416px;top:755px;width:146px}
.cal-head{display:flex;justify-content:space-between;align-items:center;font-size:11px;margin-left:-20px;width:186px;margin-bottom:11px}
.cal-head b{font-size:11px}
.arrow{width:11px;height:11px;border-radius:50%;border:1px solid #bbb;background:#eee}
.cal-grid{display:grid;grid-template-columns:repeat(7,20px);gap:1px}
.cal-grid .dow{font-size:8.5px;color:#888;text-align:center;height:12px}
.cal-grid .d{height:20px;background:var(--cal-cell);font:700 8px Arimo,sans-serif;color:#223;display:flex;align-items:center;justify-content:center}
.cal-grid .d.empty{background:#ddd}
.cal-grid .d.today{background:var(--cal-today);color:var(--white)}
.cal-tabs{display:flex;gap:3px;margin-top:4px}
.cal-tabs span{flex:1;height:15px;border:1px solid #bbb;background:#eee;font-size:9px;color:#999;display:flex;align-items:center;justify-content:center}
.video{position:absolute;left:359px;top:982px;width:263px;height:150px;border:1px solid #555}
.video .pic{height:130px;background:linear-gradient(180deg,#aab8a0 0,#7aa35a 40%,#6a9848 100%)}
.video .bar{height:19px;background:linear-gradient(#eee,#bbb);display:flex;align-items:center;gap:6px;padding:0 6px;font-size:8px}
.sponsor{position:absolute;left:670px;width:166px;display:flex;align-items:center;justify-content:center;gap:6px;font:700 14px Ubuntu,sans-serif;color:#555}
.sponsor i{width:12px;height:12px;background:#777}
.footer{position:absolute;top:1167px;font:400 11px Ubuntu,sans-serif;color:var(--white)}
.footer b{font-weight:700}
.footer-nav{left:358px;display:flex;gap:7px;font-weight:700}
</style>
</head>
<body>
<header class="header"></header>
<div class="header-rule"></div>
<div class="social" style="left:126px">Friendface</div>
<div class="social" style="left:185px;top:52px">Chirper</div>
<nav class="nav">
  <a class="current" href="#" style="left:126px">About us</a>
  <a href="#" style="left:209px">Roster</a>
  <a href="#" style="left:274px">Coaches/Staff</a>
  <a href="#" style="left:637px">Schedule</a>
  <a href="#" style="left:717px">Online Store</a>
  <a href="#" style="left:819px">Sponsors</a>
</nav>
<div class="brand"><i></i><span>VANTA</span></div>
<div class="search">
  <div class="field"><svg width="12" height="12" viewBox="0 0 12 12"><circle cx="5" cy="5" r="3.6" fill="none" stroke="#bbb" stroke-width="1.6"/><path d="M7.6 7.6 11 11" stroke="#bbb" stroke-width="1.8"/></svg>Search ...</div>
  <div class="go">Go!</div>
</div>

<main class="panel"></main>
<div class="abs ph" role="img" aria-label="Photo of a player in stance on the field with a coach nearby" style="left:139px;top:208px;width:438px;height:246px"></div>

<h2 class="abs h2" style="left:598px;top:204px">Latest Photos</h2>
<span class="abs small-link" style="left:830px;top:206px">more ▸</span>
<div class="tiles">
  <div class="tile">img</div><div class="tile">img</div><div class="tile">img</div><div class="tile">img</div>
  <div class="tile">img</div><div class="tile">img</div><div class="tile">img</div><div class="tile">img</div>
  <div class="tile">img</div><div class="tile">img</div><div class="tile">img</div><div class="tile">img</div>
</div>
<div class="hr" style="left:598px;top:437px;width:268px;border-top-style:solid;border-color:#ddd"></div>
<div class="abs" style="left:599px;top:445px;font-size:9px;color:#999">slideshow &nbsp; <span style="color:#333">ON</span> | Off</div>
<div class="vr" style="left:586px;top:208px;height:246px;border-color:#e0e0e0"></div>

<div class="hr" style="left:139px;top:470px;width:726px"></div>
<div class="hr" style="left:139px;top:502px;width:726px"></div>
<div class="vr" style="left:351px;top:470px;height:665px"></div>
<div class="vr" style="left:630px;top:470px;height:665px"></div>

<h2 class="abs h2" style="left:145px;top:478px">Lastest News</h2>
<span class="abs small-link" style="left:300px;top:481px">Archive</span>
<h2 class="abs h2 red" style="left:384px;top:478px">Recent News</h2>
<h2 class="abs h2 navy" style="left:655px;top:478px">Recent Blogs Posts</h2>
<span class="abs small-link" style="left:840px;top:481px">More</span>

<div class="news-item bullet" style="top:523px"><b>Thank you fans!</b><div class="meta">November 8th, 2010 |</div><p>Lorem ipsum dolor sit amet, consectetuer adipiscing elit</p></div>
<div class="news-item bullet" style="top:599px"><b>Thank you fans!</b><div class="meta">November 8th, 2010 |</div><p>Lorem ipsum dolor sit amet, consectetuer adipiscing elit</p></div>
<div class="news-item bullet" style="top:677px"><b>Thank you fans!</b><div class="meta">November 8th, 2010 |</div><p>Lorem ipsum dolor sit amet, consectetuer adipiscing elit</p></div>
<div class="news-item bullet" style="top:753px"><b>Thank you fans!</b><div class="meta">November 8th, 2010 |</div><p>Lorem ipsum dolor sit amet, consectetuer adipiscing elit</p></div>
<div class="news-item bullet" style="top:831px"><b>Thank you fans!</b><div class="meta">November 8th, 2010 |</div><p>Lorem ipsum dolor sit amet, consectetuer adipiscing elit</p></div>
<div class="news-item bullet" style="top:907px"><b>Thank you fans!</b><div class="meta">November 8th, 2010 |</div><p>Lorem ipsum dolor sit amet, consectetuer adipiscing elit</p></div>
<div class="news-item bullet" style="top:985px"><b>Thank you fans!</b><div class="meta">November 8th, 2010 |</div><p>Lorem ipsum dolor sit amet, consectetuer adipiscing elit</p></div>
<div class="news-item bullet" style="top:1061px"><b>Thank you fans!</b><div class="meta">November 8th, 2010 |</div><p>Lorem ipsum dolor sit amet, consectetuer adipiscing elit</p></div>

<div class="recent">
  <strong>Diam nonummy nibh euismod tincidunt</strong><br>laoreet dolore magna aliquam erat volutpat. Ut wisi enim ad minim veniam.
  <ul>
    <li class="bullet">The future of the browser</li>
    <li class="bullet">How to build a community.</li>
    <li class="bullet" style="text-decoration:underline">Using video and podcasting.</li>
    <li class="bullet">How to build quickly with Kestrelkit.</li>
  </ul>
</div>
<div class="abs" style="left:400px;top:680px;font:400 9.5px Ubuntu,sans-serif;color:#333;display:flex;gap:7px;align-items:center"><svg width="14" height="12" viewBox="0 0 14 12"><path d="M1 1h12v7H6l-3 3V8H1z" fill="#e4eef7" stroke="#9bb7d0"/></svg>Signup for our newsletter</div>

<div class="blog bullet" style="top:520px"><b>10 More Free Icon Sets</b><div class="meta">November 8th, 2008 <span style="font-family:Arimo,sans-serif">| Posted In:</span></div>Lorem ipsum dolor sit amet, consectetuer adipiscing elit</div>
<div class="blog bullet" style="top:598px"><b>10 More Free Icon Sets</b><div class="meta">November 8th, 2008 <span style="font-family:Arimo,sans-serif">| Posted In:</span></div>Lorem ipsum dolor sit amet, consectetuer adipiscing elit</div>
<div class="abs" style="left:670px;top:680px;font:400 9.5px Ubuntu,sans-serif;color:var(--orange);display:flex;gap:7px;align-items:center"><svg width="12" height="12" viewBox="0 0 12 12"><rect width="12" height="12" rx="2" fill="#e8761c"/><circle cx="3.2" cy="8.8" r="1.2" fill="#fff"/><path d="M2 5.2a4.8 4.8 0 0 1 4.8 4.8M2 2.4a7.6 7.6 0 0 1 7.6 7.6" stroke="#fff" stroke-width="1.3" fill="none"/></svg>Subscribe to our blog</div>

<div class="hr" style="left:352px;top:707px;width:513px"></div>
<div class="hr" style="left:352px;top:738px;width:513px"></div>
<h2 class="abs h2" style="left:384px;top:714px">Event Calendar</h2>
<span class="abs small-link" style="left:566px;top:718px">Past events</span>
<h2 class="abs h2" style="left:655px;top:714px">Sponsors</h2>

<div class="calendar">
  <div class="cal-head"><span class="arrow"></span><span><b>September</b> 09/09/ 2010</span><span class="arrow"></span></div>
  <div class="cal-grid">
    <span class="dow">Su</span><span class="dow">Mo</span><span class="dow">Tu</span><span class="dow">We</span><span class="dow">Th</span><span class="dow">Fr</span><span class="dow">St</span>
    <span class="d empty"></span><span class="d empty"></span><span class="d empty"></span><span class="d empty"></span><span class="d">1</span><span class="d">2</span><span class="d">3</span>
    <span class="d">4</span><span class="d">5</span><span class="d">6</span><span class="d">7</span><span class="d">8</span><span class="d today">9</span><span class="d">10</span>
    <span class="d">11</span><span class="d">12</span><span class="d">13</span><span class="d">14</span><span class="d">15</span><span class="d">16</span><span class="d">17</span>
    <span class="d">18</span><span class="d">19</span><span class="d">20</span><span class="d">21</span><span class="d">22</span><span class="d">23</span><span class="d">24</span>
    <span class="d">25</span><span class="d">26</span><span class="d">27</span><span class="d">28</span><span class="d">29</span><span class="d">30</span><span class="d">31</span>
  </div>
  <div class="cal-tabs"><span>Day</span><span>Week</span><span>Month</span></div>
</div>

<div class="hr" style="left:352px;top:941px;width:278px"></div>
<div class="hr" style="left:352px;top:972px;width:278px"></div>
<h2 class="abs h2" style="left:384px;top:948px"><span style="color:var(--red)">TOP</span> Video</h2>
<span class="abs small-link" style="left:582px;top:951px">Show all</span>
<div class="video">
  <div class="pic" role="img" aria-label="Video still of players practicing a handoff on the field"></div>
  <div class="bar">
    <svg width="10" height="10" viewBox="0 0 10 10"><path d="M1 0l9 5-9 5z" fill="#222"/></svg>
    <span style="flex:1;height:5px;background:linear-gradient(90deg,var(--red) 75%,#999 75%);margin:0 6px"></span>
    <span>0:00 / 4:20</span>
    <span style="width:46px;height:11px;background:#666"></span>
  </div>
</div>

<div class="sponsor" style="top:755px;height:80px"><i></i>Harborline Frank Stand</div>
<div class="sponsor" style="top:845px;height:85px;font-size:17px"><i></i>Delmore Press</div>
<div class="sponsor" style="top:942px;height:95px;background:#f2f2f2"><i></i>Fuelbox Westgate</div>
<div class="sponsor" style="top:1048px;height:80px"><i style="border-radius:50%"></i>Corewell Spine Studio</div>

<footer>
  <div class="footer" style="left:126px"><b>VANTA</b> © 2010 All rights reserved</div>
  <div class="footer footer-nav"><span>About us</span>•<span>Roster</span>•<span>Coaches/Staff</span>•<span>Schedule</span>•<span>Online Store</span>•<span>Sponsors</span></div>
  <div class="footer" style="left:814px;font-size:10px">To the top &nbsp;▲</div>
</footer>
</body>
</html>
```